Club Tenshiro promotional leaflet to attract new members

We are looking to produce a leaflet for a local judo club to attract seniors and juniors 5+ the leaflet needs to encourage people to attend classes and train in the martial art

Club Tenshiro are proud members of the MBA UK (mats for everyone) and practice traditional judo which mean we wear white Gi's to show cleanliness and tradition.

www.clubtenshiro.co.uk

Target Market(s)

Kids from 5+ and Adults

Font styles to use
Serif

Requirements
Must have
• Must include times of training and how to book onto a beginners induction
• it must look enticing and show that Judo is fun for all
• must highlight we open on Tuesdays and Thursdays
• Juniors are from 6.15pm to 7.15pm
• seniors 7.30pm to 9pm
• classes are held at Vantara Gym, Unit 7, Kestrel Row, Bramwick Lane, Hollowmere, East Ardley, BN19 8QT
• We practice on a Sprung floor Mat area and is great for men and women
• first two classes free
Nice to have
• Classes are run by an expeirnced team including
• Tom Harwick 5th Dan and international referee
• Neil Harwick 2nd Dan current Global Grappling Union European Champion

```html
<!DOCTYPE html>
<html lang="en">
<head>
<meta charset="utf-8">
<title>Club Tenshiro – Beginner Induction Leaflet</title>
<link href="https://fonts.googleapis.com/css2?family=Josefin+Sans:wght@300;400;600&family=Signika:wght@600;700&family=Crimson+Text&display=swap" rel="stylesheet">
<style>
  :root{
    --page-bg:#e9e6e2;
    --paper:#f4f3f1;
    --red:#b3212e;
    --red-dark:#7d1520;
    --ink:#1f1f1f;
    --ink-soft:#3a3a3a;
    --gym-dark:#2b2d31;
    --gym-light:#6d7077;
  }
  *{box-sizing:border-box;margin:0;padding:0}
  html,body{width:1200px;height:960px;overflow:hidden;background:var(--page-bg)}
  .leaflet{position:absolute;left:280px;top:20px;width:640px;height:920px;background:var(--paper);overflow:hidden;box-shadow:0 4px 18px rgba(0,0,0,.18)}
  .hero-photo{position:absolute;left:0;top:0;width:640px;height:300px;background:linear-gradient(160deg,var(--gym-light) 0%,var(--gym-dark) 70%)}
  .hero-band{position:absolute;left:0;top:150px;width:640px;height:290px}
  .photo-circle{position:absolute;border-radius:50%;border:10px solid var(--red)}
  .photo-circle--left{left:14px;top:214px;width:190px;height:190px;background:radial-gradient(circle at 50% 40%,#d9d6d2,#8a7f78)}
  .photo-circle--right{left:436px;top:214px;width:190px;height:190px;background:radial-gradient(circle at 50% 55%,#e3e1de,#9a4b4f)}
  .emblem-circle{position:absolute;left:215px;top:150px;width:210px;height:210px;border-radius:50%;background:var(--red);border:10px solid var(--red-dark)}
  .brand{position:absolute;left:0;top:436px;width:640px;display:flex;justify-content:center;align-items:center;gap:14px}
  .brand__dot{width:46px;height:46px;border-radius:50%;background:var(--red)}
  .brand__name{font-family:'Josefin Sans',sans-serif;font-weight:300;font-size:46px;letter-spacing:1px;color:var(--ink);line-height:1}
  .title{position:absolute;top:494px;width:640px;text-align:center;font-family:'Signika',sans-serif;font-weight:700;font-size:32px;line-height:1.2;color:var(--red);letter-spacing:.5px}
  .intro{position:absolute;left:40px;top:546px;width:560px;text-align:center;font-family:'Crimson Text',serif;font-size:14.5px;line-height:1.3;color:var(--ink-soft)}
  .times{position:absolute;left:34px;top:644px;width:300px;font-family:'Josefin Sans',sans-serif;color:var(--ink)}
  .times__heading{font-family:'Signika',sans-serif;font-weight:700;font-size:25px;line-height:1.2;color:var(--red);text-transform:uppercase}
  .times__days{font-family:'Signika',sans-serif;font-weight:600;font-size:19px;line-height:1.2;margin:4px 0 6px;text-transform:uppercase}
  .times__line{font-size:16px;line-height:1.3;text-transform:uppercase;letter-spacing:.5px}
  .offer{position:absolute;left:356px;top:656px;width:250px;font-family:'Josefin Sans',sans-serif;color:var(--ink)}
  .offer__suitable{font-size:13px;line-height:1.2;text-transform:uppercase;letter-spacing:.3px;white-space:nowrap}
  .offer__free{display:flex;align-items:center;gap:10px;margin-top:14px}
  .offer__small{font-size:15px;line-height:1.15;text-transform:uppercase}
  .offer__big{font-family:'Signika',sans-serif;font-weight:700;font-size:40px;color:var(--red);line-height:1}
  .offer__book{display:block;margin-top:14px;border:3px solid var(--red);padding:10px 0;text-align:center;font-family:'Signika',sans-serif;font-weight:700;font-size:18px;color:var(--red);text-transform:uppercase}
  .footer{position:absolute;left:0;bottom:0;width:640px;height:112px;background:linear-gradient(180deg,var(--red) 0%,var(--red-dark) 100%);color:#fff;font-family:'Josefin Sans',sans-serif;font-size:13.5px;text-transform:uppercase;letter-spacing:.4px;line-height:1.45}
  .footer__address{position:absolute;left:30px;top:26px;width:300px}
  .footer__contact{position:absolute;right:30px;top:16px;width:280px;text-align:right}
</style>
</head>
<body>
<main class="leaflet">
  <div class="hero-photo" role="img" aria-label="Photo of a judo throw during training in the club dojo"></div>

  <svg class="hero-band" viewBox="0 0 640 290" aria-hidden="true">
    <path d="M0 120 Q60 70 110 60 L530 60 Q580 70 640 120 L640 200 L0 200 Z" fill="#b3212e"/>
  </svg>

  <div class="photo-circle photo-circle--left" role="img" aria-label="Photo of a coach with two junior judokas in white gis"></div>
  <div class="emblem-circle"></div>
  <div class="photo-circle photo-circle--right" role="img" aria-label="Photo of the club members lined up on the mat"></div>

  <div class="brand">
    <span class="brand__dot"></span>
    <span class="brand__name">CLUB TENSHIRO</span>
  </div>

  <h1 class="title">BEGINNER INDUCTION</h1>

  <p class="intro">An excellent three level Beginners induction programme that teaches basic judo etiquette and techniques that make sure you are safe and able to participate fully in our weekly training sessions. The induction course will run over a three week time period. HOWEVER this can be accelerated based on your progression and previous experience (if any).</p>

  <section class="times">
    <h2 class="times__heading">Training Times</h2>
    <p class="times__days">Tuesday &amp; Thursday</p>
    <p class="times__line">Juniors (5 to 15 yrs old)</p>
    <p class="times__line">6.15pm to 7.15pm</p>
    <p class="times__line">Seniors (16+ unless invited)</p>
    <p class="times__line">7.30pm to 9pm</p>
  </section>

  <section class="offer">
    <p class="offer__suitable">Suitable for both women and men</p>
    <div class="offer__free">
      <span class="offer__small">Come for the<br>first 2 classes</span>
      <span class="offer__big">FREE</span>
    </div>
    <span class="offer__book">Contact us to book</span>
  </section>

  <footer class="footer">
    <p class="footer__address">Vantara Gym, Unit 7, Kestrel Row,<br>Bramwick Lane, Hollowmere,<br>East Ardley, BN19 8QT</p>
    <p class="footer__contact">Tel. 07700 900418 Email.<br>training@clubtenshiro.co.uk</p>
  </footer>
</main>
</body>
</html>
```